BUSINESS CARD DESIGN

NAME- TODD MASVERIK
PHONE NUMER - 808- 451-7082
EMAIL- OFFICE@VORLINDE-GRADEWAY.COM
BACK OF CARD- SPEACIALIZES IN LAND CLEARING, FORESTRY MUCLHING AND EXCAVATION

Contact Information for Business Card

NAME- TODD MASVERIK PHONE NUMER - 808- 451-7082 EMAIL- OFFICE@VORLINDE-GRADEWAY.COM BACK OF CARD- SPEACIALIZES IN LAND CLEARING , MUCLHING AND EXCAVATION

```html
<!DOCTYPE html>
<html lang="en">
<head>
<meta charset="utf-8">
<title>Vorlinde Gradeway LLC – Business Card</title>
<link href="https://fonts.googleapis.com/css2?family=Montserrat:wght@400;500;600&family=Lato:wght@400&display=swap" rel="stylesheet">
<style>
  :root {
    --backdrop: #6b6b6b;
    --card-dark: #1b1b1b;
    --card-dark-edge: #2a2a2a;
    --card-light: #ffffff;
    --ink: #1d2b31;
    --silver: #d6d6d6;
    --amber: #f2ae1e;
    --amber-soft: #ffd87a;
    --graphite: #3c3c3c;
    --divider: #9a9a9a;
  }
  * { margin: 0; padding: 0; box-sizing: border-box; }
  html, body { width: 1200px; height: 1000px; overflow: hidden; }
  body {
    background: var(--backdrop);
    font-family: "Montserrat", sans-serif;
    position: relative;
  }
  .card {
    position: absolute;
    left: 197px;
    width: 806px;
    height: 460px;
    border-radius: 20px;
    overflow: hidden;
  }
  .card-front {
    top: 20px;
    background: linear-gradient(160deg, var(--card-dark-edge), var(--card-dark));
  }
  .card-back {
    top: 502px;
    background: var(--card-light);
  }

  /* Front */
  .brand-lockup {
    position: absolute;
    left: 0; right: 0;
    top: 150px;
    display: flex;
    flex-direction: column;
    align-items: center;
    gap: 18px;
    color: var(--silver);
  }
  .brand-mark {
    width: 70px; height: 70px;
    border-radius: 50%;
    border: 3px solid var(--silver);
  }
  .brand-name {
    font-weight: 600;
    font-size: 34px;
    letter-spacing: 3px;
    text-align: center;
    line-height: 1.2;
  }
  .brand-phone {
    font-weight: 600;
    font-size: 22px;
    letter-spacing: 10px;
  }

  /* Back */
  .holder-name {
    position: absolute;
    left: 43px; top: 38px;
    font-weight: 500;
    font-size: 31px;
    color: var(--ink);
    letter-spacing: 0.5px;
  }
  .contact-list {
    position: absolute;
    left: 43px; top: 104px;
    list-style: none;
  }
  .contact-item {
    display: flex;
    align-items: center;
    gap: 14px;
    height: 38px;
    font-size: 22px;
    color: var(--ink);
  }
  .contact-item svg { width: 26px; height: 26px; flex: none; }

  .back-brand {
    position: absolute;
    left: 560px; top: 60px;
    width: 210px;
    display: flex;
    flex-direction: column;
    align-items: center;
    gap: 10px;
    color: var(--ink);
    text-align: center;
    font-weight: 600;
  }
  .back-brand .brand-mark { width: 48px; height: 48px; border: 3px solid var(--ink); }
  .back-brand .name { font-size: 18px; letter-spacing: 1.5px; line-height: 1.25; }

  .services {
    position: absolute;
    left: 0; top: 226px;
    width: 806px;
    display: flex;
    justify-content: center;
  }
  .service {
    width: 300px;
    display: flex;
    flex-direction: column;
    align-items: center;
    gap: 18px;
    font-family: "Lato", sans-serif;
    font-size: 19px;
    color: #111;
  }
  .service-badge {
    width: 112px; height: 112px;
    border-radius: 50%;
    background: var(--amber);
    margin-top: 6px;
  }
  .service-divider {
    width: 0;
    height: 158px;
    border-left: 2px dotted var(--divider);
    margin: 0 2px;
  }
  .card-sweep {
    position: absolute;
    left: 0; bottom: 0;
    width: 806px; height: 80px;
  }
</style>
</head>
<body>

<section class="card card-front">
  <div class="brand-lockup">
    <div class="brand-mark"></div>
    <div class="brand-name">VORLINDE GRADEWAY LLC</div>
    <div class="brand-phone">808-451-7082</div>
  </div>
</section>

<section class="card card-back">
  <h1 class="holder-name">TODD MASVERIK</h1>
  <ul class="contact-list">
    <li class="contact-item">
      <svg viewBox="0 0 24 24" fill="none" stroke="#f2ae1e" stroke-width="1.8" stroke-linecap="round" stroke-linejoin="round">
        <path d="M5 3h3l2 5-2.5 1.5a11 11 0 0 0 5 5L14 12l5 2v3a2 2 0 0 1-2 2A15 15 0 0 1 3 5a2 2 0 0 1 2-2z"/>
        <path d="M14 3h6v5h-3l-2 2v-2h-1z"/>
      </svg>
      808- 451-7082
    </li>
    <li class="contact-item">
      <svg viewBox="0 0 24 24" fill="#f2ae1e">
        <path d="M2 11 22 3l-6 18-4-7z"/>
      </svg>
      OFFICE@VORLINDE-GRADEWAY.COM
    </li>
  </ul>

  <div class="back-brand">
    <div class="brand-mark"></div>
    <div class="name">VORLINDE GRADEWAY LLC</div>
  </div>

  <div class="services">
    <div class="service">
      <div class="service-badge" role="img" aria-label="Icon of a mulching tractor beside a tree"></div>
      <span>Speacializes In Land Clearing</span>
    </div>
    <div class="service-divider"></div>
    <div class="service">
      <div class="service-badge" role="img" aria-label="Icon of a wheelbarrow full of soil"></div>
      <span>Mulching And Excavation</span>
    </div>
  </div>

  <svg class="card-sweep" viewBox="0 0 806 80" preserveAspectRatio="none">
    <defs>
      <linearGradient id="sweepGraphite" x1="0" x2="1">
        <stop offset="0" stop-color="#8a8a8a"/>
        <stop offset="1" stop-color="#1f1f1f"/>
      </linearGradient>
      <linearGradient id="sweepAmber" x1="0" x2="1">
        <stop offset="0" stop-color="#ffe7a8"/>
        <stop offset="1" stop-color="#f2ae1e"/>
      </linearGradient>
    </defs>
    <path d="M0 18 C110 26 210 50 290 80 L0 80 Z" fill="url(#sweepGraphite)"/>
    <path d="M170 8 C220 40 290 60 420 56 C560 52 700 20 806 6 L806 80 L300 80 C250 60 210 30 170 8 Z" fill="url(#sweepAmber)"/>
  </svg>
</section>

</body>
</html>
```